Online eyewear company needs a couple Sign-In and Product Review page designs

We sell prescription glasses starting at $99 with Free Shipping. We have over 300 different styles and colors.Our website is under construction and we need an amazing Sign-In and Product Review Pages to help finish things off. Our brand is called VEROK and our website is called VEROKEYEWEAR.COM.

We need 5 simple sign-in and product review pages to help finish our website. Sample pages attached

We need the pages to go in order

Quick Checkout review
Sign-In
Prescription
Shipping & Payment
Final Review

Target Market(s)

20-50 that wears glasses

Industry/Entity Type

Eyewear

Colors
ffffff
919191
eaeaea
d3d3d3
dddddd
b7b7b7
000000
3176b5

Requirements
Must have
• Simple, creative, original. Must not be exactly like the photos attached. They're just templete of our casual, simple style.
• We need the pages to go in order
• Quick Checkout review
• Sign-In
• Prescription
• Shipping & Payment
• Final Review
Should not have
• Must not look exactly like the photos attached.

```html
<!DOCTYPE html>
<html lang="en">
<head>
<meta charset="utf-8">
<title>VEROK – Final Review</title>
<link href="https://fonts.googleapis.com/css2?family=Lato:wght@400;700&family=Open+Sans:ital,wght@0,400;0,600;0,700;1,400&display=swap" rel="stylesheet">
<style>
  :root{
    --white:#ffffff;
    --grey-mid:#919191;
    --grey-light:#eaeaea;
    --grey-line:#d3d3d3;
    --grey-soft:#dddddd;
    --grey-step:#b7b7b7;
    --ink:#000000;
    --text:#333333;
    --muted:#6b6b6b;
    --blue:#3176b5;
    --link:#8aa7cc;
    --badge:#d6157f;
    --footer:#3b3b3b;
  }
  *{box-sizing:border-box;margin:0;padding:0}
  html,body{width:1200px;height:1189px;overflow:hidden;background:var(--white)}
  body{position:relative;font-family:"Open Sans",sans-serif;color:var(--text)}
  .abs{position:absolute}

  .promo-bar{left:0;top:0;width:1200px;height:31px;background:var(--grey-light);
    font:400 10px/31px "Lato",sans-serif;text-align:center;color:var(--ink)}
  .site-header{left:0;top:31px;width:1200px;height:57px;border-bottom:1px solid var(--grey-soft)}
  .brand{left:90px;top:11px;font:400 22px/1 "Lato",sans-serif;letter-spacing:4px;color:var(--ink)}
  .main-nav{left:281px;top:22px;display:flex;gap:19px;font:400 13px/1 "Lato",sans-serif;color:var(--text)}
  .utility-nav{left:1028px;top:24px;display:flex;align-items:center;gap:6px;font:400 11.5px/1 "Lato",sans-serif;color:var(--muted)}
  .utility-nav .sep{color:var(--blue)}
  .cart{left:1150px;top:11px;width:34px;height:35px;border-radius:7px;background:var(--white);
    box-shadow:0 1px 4px rgba(0,0,0,.35);display:flex;align-items:center;justify-content:center}
  .cart-badge{left:1140px;top:3px;width:16px;height:16px;border-radius:50%;background:var(--badge);
    color:var(--white);font:400 8px/16px "Open Sans",sans-serif;text-align:center}

  .steps{left:247px;top:131px;display:flex;gap:7px}
  .step{width:231px;height:30px;background:var(--grey-light);color:var(--white);
    font:400 10px/30px "Open Sans",sans-serif;text-align:center;position:relative}
  .step.is-active{background:var(--grey-step);font-weight:600}
  .step.is-active::after{content:"";position:absolute;left:50%;bottom:-6px;margin-left:-6px;
    border:6px solid transparent;border-bottom:0;border-top-color:var(--grey-step)}

  .section-label{font:600 13px/1 "Open Sans",sans-serif;color:var(--ink)}
  .section-label .edit{font:italic 400 9px/1 "Open Sans",sans-serif;color:var(--link);margin-left:4px}

  .rx-table{left:248px;top:242px;width:280px;border-collapse:collapse;font-size:7px;color:var(--muted)}
  .rx-table th,.rx-table td{border:1px solid var(--grey-mid);text-align:center;font-weight:400}
  .rx-table th{height:27px;background:var(--grey-light);letter-spacing:1.2px}
  .rx-table td{height:28px}
  .rx-table td.eye{text-align:left;padding-left:7px;color:var(--text)}
  .pd-row{left:248px;top:333px;width:280px;height:28px;border:1px solid var(--grey-mid);display:flex;font-size:7px;color:var(--muted)}
  .pd-row>div{display:flex;align-items:center;justify-content:center;gap:10px}
  .pd-row .pd-label{width:122px;border-right:1px solid var(--grey-mid);color:var(--text)}
  .pd-row .pd-side{width:80px;border-right:1px solid var(--grey-mid)}
  .pd-row .pd-side:last-child{border-right:0;flex:1}
  .pd-row b{font-weight:400;color:var(--text)}

  .info-box{left:248px;width:280px;border:1px solid var(--grey-mid)}
  .address{top:417px;height:83px;padding:17px 0 0 23px;font-size:12.5px;line-height:16px;color:var(--ink)}
  .payment{top:557px;height:82px;display:flex;align-items:center;padding-left:31px;gap:26px}
  .card-name{font:700 11px/1 "Open Sans",sans-serif;color:var(--blue)}
  .card-meta{font-size:10px;line-height:12.5px;color:var(--ink);display:grid;grid-template-columns:auto auto;column-gap:12px}

  .column-divider{left:574px;top:206px;width:1px;height:735px;background:var(--grey-mid)}

  .rule{left:620px;width:334px;height:1px;background:var(--grey-soft)}
  .product-visual{left:632px;width:296px;height:88px;border-radius:40px;
    background:radial-gradient(ellipse at 25% 50%,rgba(110,70,50,.35),transparent 45%),
               radial-gradient(ellipse at 75% 50%,rgba(110,70,50,.35),transparent 45%),#f7f4f2}
  .product-name{left:656px;font:400 16px/1 "Open Sans",sans-serif;color:var(--text)}
  .product-colour{left:656px;font:italic 400 9.5px/1 "Open Sans",sans-serif;color:var(--muted)}
  .product-price{font:400 13px/1 "Open Sans",sans-serif;color:var(--text)}

  .summary{left:620px;top:594px;width:334px;height:169px;background:var(--grey-light);padding:17px 20px 0 12px}
  .summary h2{font:600 17px/1 "Open Sans",sans-serif;color:var(--text);letter-spacing:.5px}
  .summary-row{display:flex;justify-content:space-between;padding-left:3px;font-size:10.5px;color:var(--muted);letter-spacing:.5px}
  .summary-row strong{font-weight:600;color:var(--text);font-size:10px;letter-spacing:0}
  .summary .sub{margin-top:21px}
  .summary .ship{margin-top:13px}
  .summary hr{border:0;height:1px;background:var(--grey-mid);margin:16px -6px 0 3px}
  .summary .total{margin-top:17px;font:600 15px/1 "Open Sans",sans-serif;letter-spacing:1.8px;color:var(--text)}
  .summary .total strong{font-size:15px;letter-spacing:0}

  .place-order{left:621px;top:777px;width:333px;height:63px;background:var(--blue);border:0;
    color:var(--white);font:400 16px/63px "Open Sans",sans-serif;text-align:center}
  .order-note{left:620px;top:850px;width:334px;text-align:center;font:italic 400 7px/1 "Open Sans",sans-serif;color:var(--muted)}
  .terms{left:620px;top:884px;width:334px;text-align:center;font-size:8.5px;line-height:11.5px;color:var(--muted)}
  .terms a{color:var(--blue);text-decoration:none}

  .site-footer{left:0;top:982px;width:1200px;height:207px;background:var(--footer)}
  .footer-backdrop{left:0;top:0;width:1200px;height:207px;
    background:radial-gradient(ellipse at 30% 60%,rgba(255,255,255,.07),transparent 40%),
               radial-gradient(ellipse at 72% 60%,rgba(255,255,255,.07),transparent 40%)}
  .footer-brand{left:250px;top:47px;font:400 38px/1 "Lato",sans-serif;letter-spacing:7px;color:var(--white)}
  .footer-col{top:56px;width:170px}
  .footer-col h3{font:700 14px/1 "Lato",sans-serif;color:var(--white);letter-spacing:-.3px;margin-bottom:14px}
  .footer-col li{list-style:none;font:400 12px/22px "Lato",sans-serif;color:#d8d8d8}
</style>
</head>
<body>

<div class="abs promo-bar">FREE SHIPPING IN CONTINENTAL US</div>

<header class="abs site-header">
  <div class="abs brand">VEROK</div>
  <nav class="abs main-nav"><span>EYEGLASSES</span><span>ORDER LENSES</span></nav>
  <div class="abs utility-nav">
    <svg width="12" height="12" viewBox="0 0 12 12" aria-hidden="true"><circle cx="5" cy="5" r="4" fill="none" stroke="#919191" stroke-width="1.6"/><line x1="8" y1="8" x2="11" y2="11" stroke="#919191" stroke-width="1.8"/></svg>
    <span>SEARCH</span><span class="sep">|</span><span>HELP</span>
  </div>
</header>
<div class="abs cart">
  <svg width="20" height="16" viewBox="0 0 20 16" aria-label="Cart"><path d="M1 6h18l-2.5 9h-13z" fill="#000"/><path d="M5 6l4-5M15 6l-4-5" stroke="#000" stroke-width="1.6" fill="none"/><circle cx="7" cy="10" r="1" fill="#fff"/><circle cx="10" cy="10" r="1" fill="#fff"/><circle cx="13" cy="10" r="1" fill="#fff"/></svg>
</div>
<div class="abs cart-badge">2</div>

<div class="abs steps">
  <div class="step">Prescription</div>
  <div class="step">Shipping &amp; Payment</div>
  <div class="step is-active">Final Review</div>
</div>

<div class="abs section-label" style="left:248px;top:222px">Prescription: <span class="edit">(Edit)</span></div>
<table class="abs rx-table">
  <tr><th style="width:72px"></th><th>SPH</th><th>CYL</th><th>AXIS</th><th>ADD</th></tr>
  <tr><td class="eye">Right Eye (OD)</td><td>-1.75</td><td>-0.75</td><td>090</td><td>+1.00</td></tr>
  <tr><td class="eye">Left Eye (OS)</td><td>-1.75</td><td>-0.75</td><td>090</td><td>+1.00</td></tr>
</table>
<div class="abs pd-row">
  <div class="pd-label">Pupillary Distance (PD)</div>
  <div class="pd-side">RIGHT: <b>24.0</b></div>
  <div class="pd-side">LEFT: <b>24.0</b></div>
</div>

<div class="abs section-label" style="left:248px;top:397px">Shipping Address: <span class="edit">(Edit)</span></div>
<div class="abs info-box address">
  <div>John Doe</div>
  <div style="margin-top:3px">Contact Details</div>
  <div>Address Address Address</div>
</div>

<div class="abs section-label" style="left:248px;top:536px">Payment Method: <span class="edit">(Edit)</span></div>
<div class="abs info-box payment">
  <span class="card-name">PAYCARD</span>
  <div class="card-meta"><span>Ending:</span><span>0592</span><span>Expires:</span><span>2024</span></div>
</div>

<div class="abs column-divider"></div>

<div class="abs rule" style="top:226px"></div>
<div class="abs product-visual" style="top:236px" role="img" aria-label="Brown metal eyeglass frames, front view"></div>
<div class="abs product-name" style="top:340px">Halloway</div>
<div class="abs product-colour" style="top:356px">Brown</div>
<div class="abs product-price" style="left:854px;top:348px">$99.00</div>
<div class="abs rule" style="top:385px"></div>
<div class="abs product-visual" style="top:412px" role="img" aria-label="Brown metal eyeglass frames, front view"></div>
<div class="abs product-name" style="top:511px">Halloway</div>
<div class="abs product-colour" style="top:527px">Brown</div>
<div class="abs product-price" style="left:846px;top:517px">$253.00</div>
<div class="abs rule" style="top:562px"></div>

<section class="abs summary">
  <h2>Order Summary</h2>
  <div class="summary-row sub"><span>SUB TOTAL &nbsp;&nbsp;(2) Items</span><strong>$352</strong></div>
  <div class="summary-row ship"><span>SHIPPING FEE</span><strong>FREE</strong></div>
  <hr>
  <div class="summary-row total"><span>TOTAL</span><strong>$352</strong></div>
</section>

<div class="abs place-order">Place Order</div>
<div class="abs order-note">Free of Standard Shipping (CONTINENTAL US) and free return on all orders.</div>
<div class="abs terms">By placing this order, you agree to our<br><a href="#">Terms of Use</a> and <a href="#">Privacy Policy</a>.</div>

<footer class="abs site-footer">
  <div class="abs footer-backdrop" role="img" aria-label="Faint photo of clear eyeglass frames in the background"></div>
  <div class="abs footer-brand">VEROK</div>
  <div class="abs footer-col" style="left:458px"><h3>PRODUCTS</h3><ul>
    <li>Men's Frames</li><li>Women's Frames</li><li>New Arrivals</li><li>Best Sellers</li><li>Featured Frames</li></ul></div>
  <div class="abs footer-col" style="left:636px"><h3>ORDER</h3><ul>
    <li>Single Vision Lenses</li><li>Blue Light Blocking</li><li>Computer Lenses</li><li>High Index Lenses</li><li>Transition Lenses</li><li>Reading Lenses</li></ul></div>
  <div class="abs footer-col" style="left:814px"><h3>INFORMATION</h3><ul>
    <li>Track Order</li><li>About Us</li><li>Contact Us</li><li>Returns</li><li>Warranty</li><li>FAQ</li></ul></div>
</footer>

</body>
</html>
```